Bref créative
Birchwell Guard Networks LLC
home automation at it finest
Professional
LEONARDO MASRIVEN
COO
4185 WILLOW CREST AVE
SUITE 318
LARKHAVEN CO 80417
866-503-2718 ex 4
leo@doverlinkgroup.example

```html
<!DOCTYPE html>
<html lang="en">
<head>
<meta charset="utf-8">
<title>Birchwell Guard Networks – Stationery</title>
<link href="https://fonts.googleapis.com/css2?family=Arimo:wght@400;700&display=swap" rel="stylesheet">
<style>
  :root {
    --stage: #9c9c9c;
    --paper: #ffffff;
    --navy: #1f3a6b;
    --ink: #3a3a3a;
    --fold: #e3e3e3;
  }
  * { margin: 0; padding: 0; box-sizing: border-box; }
  html, body { width: 1200px; height: 655px; overflow: hidden; }
  body {
    background: var(--stage);
    font-family: "Arimo", Arial, sans-serif;
    color: var(--ink);
    position: relative;
  }
  .sheet {
    position: absolute;
    background: var(--paper);
    box-shadow: 0 1px 3px rgba(0,0,0,.25);
  }
  .brand {
    display: flex;
    align-items: center;
    gap: 6px;
    color: var(--navy);
    font-weight: 700;
    text-transform: uppercase;
    line-height: 1;
    white-space: nowrap;
  }
  .brand__mark { background: var(--navy); flex: none; }
  .contact-line { white-space: nowrap; color: var(--navy); }

  /* Letterhead */
  .letterhead { left: 168px; top: 12px; width: 432px; height: 636px; }
  .letterhead .brand { position: absolute; left: 24px; top: 28px; font-size: 15px; }
  .letterhead .brand__mark { width: 20px; height: 20px; }
  .letterhead .contact-line { position: absolute; left: 24px; bottom: 26px; font-size: 6px; }

  /* Business card */
  .business-card { left: 24px; top: 276px; width: 164px; height: 108px; }
  .business-card .brand { position: absolute; left: 10px; top: 10px; font-size: 7px; gap: 4px; }
  .business-card .brand__mark { width: 10px; height: 10px; }
  .business-card .person { position: absolute; left: 0; right: 0; top: 46px; text-align: center; }
  .person__name { font-size: 7px; color: var(--navy); font-weight: 700; }
  .person__title { font-size: 5px; margin-top: 2px; }
  .business-card .details {
    position: absolute; left: 10px; right: 10px; bottom: 8px;
    font-size: 4.5px; line-height: 1.5; white-space: nowrap;
  }

  /* Envelope back */
  .envelope-back { left: 655px; top: 84px; width: 526px; height: 228px; overflow: hidden; }
  .envelope-back svg { position: absolute; left: 0; top: 0; }
  .envelope-back .seal-mark {
    position: absolute; left: 253px; top: 33px; width: 20px; height: 20px; background: var(--navy);
  }

  /* Envelope front */
  .envelope-front { left: 655px; top: 343px; width: 526px; height: 226px; }
  .envelope-front .brand { position: absolute; left: 30px; top: 28px; font-size: 15px; }
  .envelope-front .brand__mark { width: 20px; height: 20px; }
  .envelope-front .email { position: absolute; right: 28px; top: 16px; font-size: 6.5px; color: var(--navy); }
  .envelope-front .contact-line { position: absolute; left: 30px; bottom: 26px; font-size: 6.5px; }
</style>
</head>
<body>

  <section class="sheet letterhead" aria-label="Letterhead">
    <div class="brand"><span class="brand__mark"></span><span class="brand__name">Birchwell Guard Networks</span></div>
    <p class="contact-line">A: Larkhaven CO 80417 4185 Willow Crest Ave Suite 318 &nbsp; P: 866-503-2718 ex 4 &nbsp; F: 866-503-2790 &nbsp; E: info@doverlinkgroup.example</p>
  </section>

  <section class="sheet business-card" aria-label="Business card">
    <div class="brand"><span class="brand__mark"></span><span class="brand__name">Birchwell Guard Networks</span></div>
    <div class="person">
      <p class="person__name">LEONARDO MASRIVEN</p>
      <p class="person__title">COO</p>
    </div>
    <div class="details">
      <p>4185 WILLOW CREST AVE SUITE 318 LARKHAVEN CO 80417</p>
      <p>P: 866-503-2718 ex 4 &nbsp; E: leo@doverlinkgroup.example</p>
    </div>
  </section>

  <section class="sheet envelope-back" aria-label="Envelope back">
    <svg width="526" height="228" viewBox="0 0 526 228">
      <path d="M0 0 L0 40 Q10 58 60 70 Q263 110 466 70 Q516 58 526 40 L526 0 Z" fill="var(--paper)" stroke="var(--fold)" stroke-width="1.5"/>
    </svg>
    <span class="seal-mark"></span>
  </section>

  <section class="sheet envelope-front" aria-label="Envelope front">
    <div class="brand"><span class="brand__mark"></span><span class="brand__name">Birchwell Guard Networks</span></div>
    <p class="email">info@doverlinkgroup.example</p>
    <p class="contact-line">A: Larkhaven CO 80417 4185 Willow Crest Ave Suite 318 &nbsp; P: 866-503-2718 ex 4 &nbsp; F: 866-503-2790</p>
  </section>

</body>
</html>
```